Wordpress design for my private practice website - Psychotherapist

I would like a simple, clean, and elegant design for my private practice website. I work with both adults and children so I'd like it to appeal to both. However, since parents make the choice as to where to send their child for therapy, I want it to appeal to adults more. I would like the pictures on the site to have a calming effect - maybe using sand and water and rocks. I am attaching files with my company logo. I would also like my name incorporated into the header - Colette Brannigan, LCSW, Registered Play Therapist. I've also uploaded a picture of myself for my About Page.

I like the design of these 2 website and want something similar:
www.drlorapenwick.example
www.harwood-tallis.example

I would like a home page that highlights a calming graphic across the entire top of the page as well as my practice logo and my name.

I'd like a link to social media sites on the top of the homepage - facebook, pinterest.

I want a simple bar across the top with the following tabs:
Home
About Me (subtabs Who I Am, Specialties and Approach)
Counseling Services (subtabs Individual Counseling, Play Therapy, Sandplay Therapy,)
Fees
FAQs
Contact Me (would love this to be a fill in the blank contact form that sends info to my email address - should include name, phone number, email and a comment box for more information requested)
Blog (this will link with another wordpress blog)

Target Market(s)

Parents of children under age 12 with behavioral problems or are dealing with the breakup of their family through divorce - looking for someone to work with their young child. I also work with Adults that are overwhelmed and worried - often women that have many life stressors and are feeling burnt out on life and meeting everyone's needs. Families going through some type of trauma, including divorce or grief work. I also work with individuals going through a transition of religious beliefs - often exiting the religion of their youth and undergoing a crisis of faith at midlife.

Industry/Entity Type

Mental Health

Contact Information for Business Card

Colette Brannigan, LCSW
Registered Play Therapist
4917 Wexmoor Lane
Idaho Falls, Idaho 83404
(208)555-0187
www.stillbrookcounseling.example

On the opposite side, I'd like an appointment reminder area - with the following text:

Your next appointment is
_____/______/______ at ______am/pm
Please give 24 hrs notice if you need to cancel your appointment.

Coding

Coded - Design and coding required

Number of Pages Required

5+ page

Font styles to use
Sans Serif

Colors
33a6d7
9bcb3c
0355a3

Requirements
Must have
• I'd like it to be a wordpress site. I'm such a newby at web design - but I need to be able to add content and manage the site myself once it is up and running.
Nice to have
• I like the design of these 2 websites and want something similar:
• www.drlorapenwick.example
• www.harwood-tallis.example
• They are clean, easy to navigate and calming.
Should not have
• Should not look like a childcare website.

```html
<!DOCTYPE html>
<html lang="en">
<head>
<meta charset="utf-8">
<title>Stillbrook Counseling</title>
<link href="https://fonts.googleapis.com/css2?family=Roboto:wght@300;400;500;700&display=swap" rel="stylesheet">
<style>
:root{
  --blue:#33a6d7;
  --blue-deep:#1f5a93;
  --green:#9bcb3c;
  --navy:#0355a3;
  --ink:#1d1d1d;
  --text:#6b6b6b;
  --muted:#8a8a8a;
  --band:#f4f4f4;
  --footer:#1f1f1f;
  --white:#ffffff;
}
*{margin:0;padding:0;box-sizing:border-box}
html,body{width:1200px;height:2410px;overflow:hidden}
body{font-family:"Roboto",Arial,sans-serif;color:var(--text);background:var(--white);position:relative}
.abs{position:absolute}

/* Hero */
.hero{position:absolute;left:0;top:0;width:1200px;height:485px;
  background:linear-gradient(180deg,#1c2a3a 0%,#2b3d52 55%,#33465a 80%,#2a3644 100%)}
.hero-stones{position:absolute;left:300px;top:80px;width:620px;height:405px;
  background:radial-gradient(ellipse at 50% 60%,rgba(120,115,108,.55) 0%,rgba(80,78,74,.35) 45%,rgba(40,50,60,0) 72%)}
.hero-name{left:106px;top:214px;color:var(--white);font-weight:500;font-size:16px;line-height:27px}
.brand{left:400px;top:258px;width:400px;text-align:center;color:var(--white)}
.brand-dot{display:block;width:22px;height:22px;border-radius:50%;background:var(--green);margin:0 auto 12px}
.brand-name{font-size:22px;font-weight:300;letter-spacing:4px;line-height:26px}
.brand-sub{font-size:11px;font-weight:300;letter-spacing:4px;margin-top:4px}
.social-top{top:233px;display:flex;gap:16px;left:1048px}
.sq{display:block;width:19px;height:19px;border-radius:3px;background:var(--white)}
.hero-arrows{left:566px;top:430px;display:flex;gap:14px}

/* Nav */
.nav{position:absolute;left:0;top:485px;width:1200px;height:56px;background:var(--blue)}
.nav ul{list-style:none;position:absolute;left:217px;top:0;height:56px;display:flex}
.nav li{height:56px;line-height:56px;color:var(--white);font-size:12px;font-weight:500;padding:0 28px}
.nav li.active{background:var(--blue-deep)}

/* About */
.photo-frame{left:100px;top:599px;width:359px;height:410px;background:#ececec;padding:16px}
.photo{width:100%;height:100%;border:3px solid var(--white);
  background:linear-gradient(160deg,#d9bd83 0%,#c8a46a 40%,#8f8a5c 75%,#5f6a3e 100%)}
.about{left:506px;top:597px;width:597px}
.about h1{color:var(--ink);font-size:24px;font-weight:500;line-height:30px}
.about .lead{color:var(--ink);font-size:17px;margin-top:8px}
.about p.body{font-size:11px;line-height:20px;margin-top:14px;color:var(--muted)}
.btn{display:inline-block;background:var(--green);color:var(--white);font-size:11px;font-weight:500;
  text-align:center;border-radius:2px}
.about .btn{position:absolute;left:0;top:375px;width:111px;height:38px;line-height:38px}

/* Features */
.features{position:absolute;left:0;top:1068px;width:1200px;height:402px;background:var(--band)}
.feature{position:absolute;top:52px;width:280px;text-align:center}
.feature .ring{width:160px;height:160px;border-radius:50%;background:#c6c6c6;margin:0 auto;position:relative}
.feature .ring.on{background:#d4e9f3}
.feature .core{position:absolute;left:16px;top:16px;width:128px;height:128px;border-radius:50%;background:#2a2a2a}
.feature .ring.on .core{background:var(--blue)}
.feature .core svg{position:absolute;left:40px;top:40px}
.feature h2{color:var(--ink);font-size:18px;font-weight:500;margin-top:32px}
.feature p{font-size:11px;line-height:19px;color:var(--muted);margin:12px auto 0;width:220px}
.feature .btn{width:111px;height:36px;line-height:36px;margin-top:20px}

/* Newsletter */
.newsletter{position:absolute;left:0;top:1470px;width:1200px;height:237px;
  background:linear-gradient(90deg,#2e3134 0%,#3c3a38 30%,#34373a 60%,#2a2e31 100%)}
.newsletter h2{position:absolute;top:36px;width:1200px;text-align:center;color:var(--white);font-size:24px;font-weight:500}
.newsletter p{position:absolute;top:91px;width:1200px;text-align:center;color:#e6e6e6;font-size:13px}
.news-input{left:278px;top:139px;width:549px;height:56px;background:var(--white);font-size:11px;color:#444;padding:0 18px;line-height:56px}
.news-send{left:827px;top:139px;width:93px;height:56px;background:var(--blue);color:var(--white);text-align:center;line-height:56px;font-size:16px;font-weight:500}

/* Featured links */
.featured-title{left:0;top:1748px;width:1200px;text-align:center;color:#333;font-size:24px;font-weight:500}
.post{position:absolute;top:1818px;width:322px}
.post .img{height:219px;border:3px solid #e8e8e8;position:relative}
.post .date{position:absolute;left:0;bottom:0;width:70px;height:70px;background:var(--blue);color:var(--white);text-align:center}
.post .date small{display:block;font-size:10px;padding-top:8px}
.post .date b{display:block;font-size:28px;font-weight:400;line-height:38px}
.post h3{color:var(--ink);font-size:14px;font-weight:500;margin-top:34px}
.post p{font-size:11px;line-height:19px;color:#555;margin-top:10px}
.post .more{display:block;font-size:11px;font-style:italic;color:var(--green);margin-top:14px}
.slide-arrow{top:1895px}

/* Footer */
.footer{position:absolute;left:0;top:2237px;width:1200px;height:173px;background:var(--footer)}
.footer-social{position:absolute;left:507px;top:36px;display:flex;gap:37px}
.footer-social .sq{width:22px;height:22px;background:var(--green)}
.footer-contact{position:absolute;top:86px;width:1200px;text-align:center;color:var(--white);font-size:14px}
.footer-contact span{margin:0 12px;color:#bbb}
.footer-copy{position:absolute;top:126px;width:1200px;text-align:center;color:#bdbdbd;font-size:11px}
</style>
</head>
<body>

<header class="hero">
  <div class="hero-stones" role="img" aria-label="Photograph of smooth grey stones balanced in an arch against a dark sea sky"></div>
  <div class="abs hero-name">Colette Brannigan, LCSW,<br>Registered Play Therapist</div>
  <div class="abs brand">
    <span class="brand-dot"></span>
    <div class="brand-name">STILLBROOK</div>
    <div class="brand-sub">COUNSELING</div>
  </div>
  <div class="abs social-top"><span class="sq"></span><span class="sq"></span></div>
  <div class="abs hero-arrows">
    <svg width="28" height="28" viewBox="0 0 28 28"><circle cx="14" cy="14" r="12.5" fill="none" stroke="#9aa4ad" stroke-width="1.5"/><path d="M18 14H9m4-4-4 4 4 4" fill="none" stroke="#9aa4ad" stroke-width="1.5"/></svg>
    <svg width="28" height="28" viewBox="0 0 28 28"><circle cx="14" cy="14" r="12.5" fill="none" stroke="#9aa4ad" stroke-width="1.5"/><path d="M10 14h9m-4-4 4 4-4 4" fill="none" stroke="#9aa4ad" stroke-width="1.5"/></svg>
  </div>
</header>

<nav class="nav">
  <ul>
    <li class="active">HOME</li>
    <li>ABOUT ME</li>
    <li>COUNSELING SERVICES</li>
    <li>FEES</li>
    <li>FAQS</li>
    <li>CONTACT</li>
    <li>BLOG</li>
  </ul>
</nav>

<section>
  <div class="abs photo-frame"><div class="photo" role="img" aria-label="Portrait photograph of the therapist outdoors in warm grass"></div></div>
  <div class="abs about">
    <h1>MAINTENANCE PAGE</h1>
    <p class="lead">This website is currently down for maintenance. Please come back soon.</p>
    <p class="body">If you are looking for extra support and guidance through a difficult season or you are simply ready to move in a new direction in your life, I look forward to working with you to reach your goals.</p>
    <p class="body" style="margin-top:8px">Please call or email me for an individual, couples or family therapy consultation today. I work with a wide range of emotional and behavioral concerns, providing services that span from therapy for anxiety and grief counseling to parenting support, couples counseling and beyond. In a comfortable and supportive atmosphere, I offer a highly personalized approach tailored to each of my clients and their needs to help reach the personal growth they are striving for. Sessions move at your own pace, and together we look for small, steady steps toward calm. Children are welcomed through play, sand and art, while adults find space to slow down, breathe and be heard. Families facing divorce, loss or change can rebuild trust and learn new ways to listen to one another. Whatever brings you here, you do not have to carry it alone, and every question is welcome before we begin our first meeting together in the office.</p>
    <span class="btn">READ MORE</span>
  </div>
</section>

<section class="features">
  <div class="feature" style="left:101px">
    <div class="ring"><div class="core">
      <svg width="48" height="48" viewBox="0 0 48 48" fill="none" stroke="#fff" stroke-width="2"><path d="M24 12a9 9 0 0 0-5 16.5V33h10v-4.5A9 9 0 0 0 24 12z"/><path d="M20 37h8M21 40h6M24 4v4M10 10l3 3M38 10l-3 3M6 22h4M38 22h4"/></svg>
    </div></div>
    <h2>SCHEDULE APPOINTMENT</h2>
    <p>Start your new path in life and be the change today!</p>
    <span class="btn">READ MORE</span>
  </div>
  <div class="feature" style="left:474px">
    <div class="ring on"><div class="core">
      <svg width="48" height="48" viewBox="0 0 48 48" fill="#fff"><circle cx="18" cy="14" r="7"/><path d="M4 40c0-9 6-15 14-15s11 4 12 7v8z"/><circle cx="35" cy="33" r="7" fill="none" stroke="#fff" stroke-width="3"/><circle cx="35" cy="33" r="2.5"/></svg>
    </div></div>
    <h2>LINKS &amp; RESOURCES</h2>
    <p>View recommended websites and other valuable resources.</p>
    <span class="btn">READ MORE</span>
  </div>
  <div class="feature" style="left:846px">
    <div class="ring"><div class="core">
      <svg width="48" height="48" viewBox="0 0 48 48" fill="#fff"><circle cx="24" cy="11" r="6"/><path d="M14 28c0-6 4-10 10-10s10 4 10 10z"/><circle cx="13" cy="26" r="5"/><circle cx="35" cy="26" r="5"/><path d="M4 42c0-6 4-9 9-9s9 3 9 9zM26 42c0-6 4-9 9-9s9 3 9 9z"/></svg>
    </div></div>
    <h2>HELPFUL FORMS</h2>
    <p>Click here to view and print forms for your appointment.</p>
    <span class="btn">READ MORE</span>
  </div>
</section>

<section class="newsletter" role="img" aria-label="Dimmed background photograph of a busy street of cars">
  <h2>NEWSLETTER</h2>
  <p>Lorem Ipsum, you need to be sure there isn't anything embarrassing hidden</p>
  <div class="abs news-input">Enter Your Email :</div>
  <div class="abs news-send">SEND</div>
</section>

<section>
  <h2 class="abs featured-title">FEATURED SITE LINKS</h2>
  <svg class="abs slide-arrow" style="left:68px" width="24" height="96" viewBox="0 0 24 96"><path d="M22 2 2 48l20 46" fill="none" stroke="#c9c9c9" stroke-width="2"/></svg>
  <svg class="abs slide-arrow" style="left:1108px" width="24" height="96" viewBox="0 0 24 96"><path d="M2 2l20 46L2 94" fill="none" stroke="#c9c9c9" stroke-width="2"/></svg>

  <article class="post" style="left:100px">
    <div class="img" role="img" aria-label="Photograph of rust coloured rocks on a sandy beach under a blue sky" style="background:linear-gradient(180deg,#9fcfe8 0%,#cfe3ea 35%,#c98a52 60%,#8a5a38 100%)">
      <div class="date"><small>Jan</small><b>05</b></div>
    </div>
    <h3>LIST OF BEST FOOTBALL TRICKS</h3>
    <p>That's the promise we need to keep. I will build new partnerships to defeat the threats of the 21st century: terrorism and nuclear proliferation; poverty and genocide; climate change and disease.</p>
    <span class="more">READ MORE</span>
  </article>
  <article class="post" style="left:438px">
    <div class="img" role="img" aria-label="Photograph of a pebble shore and calm blue sea with a rocky headland" style="background:linear-gradient(180deg,#4d82b8 0%,#2f6aa0 45%,#7d8f96 62%,#a39c92 100%)">
      <div class="date"><small>Jan</small><b>08</b></div>
    </div>
    <h3>NAMED THE WORST PLAYER OF</h3>
    <p>That's the promise we need to keep. I will build new partnerships to defeat the threats of the 21st century: terrorism and nuclear proliferation; poverty and genocide; climate change and disease.</p>
    <span class="more">READ MORE</span>
  </article>
  <article class="post" style="left:777px">
    <div class="img" role="img" aria-label="Photograph of many raised hands giving a thumbs up against a sky" style="background:linear-gradient(160deg,#5cc3d9 0%,#9fdbe6 45%,#d8a98a 75%,#c98e6c 100%)">
      <div class="date"><small>Jan</small><b>12</b></div>
    </div>
    <h3>THE MOST EPIC MATCH OF THE SEASON</h3>
    <p>That's the promise we need to keep. I will build new partnerships to defeat the threats of the 21st century: terrorism and nuclear proliferation; poverty and genocide; climate change and disease.</p>
    <span class="more">READ MORE</span>
  </article>
</section>

<footer class="footer">
  <div class="footer-social"><span class="sq"></span><span class="sq"></span><span class="sq"></span><span class="sq"></span></div>
  <div class="footer-contact">4917 Wexmoor Lane, Idaho Falls, Idaho<span>|</span>(208)555-0187 / (208)555-0142<span>|</span>info@stillbrookcounseling.example</div>
  <div class="footer-copy">© Copy Rights 2016 - stillbrookcounseling.example - all rights reserved</div>
</footer>

</body>
</html>
```